Letterbox drop flyers for local business

I need a flyer design for my small business located in Canberra ACT called "Tallowbend Garden Care" My company is a landscaping business offering garden design, landscaping services, garden maintenance and horticultural services. I would like to have a flyer I can leave at nurseries and do letterbox drops with that highlight the professional quality of our services and also our brand feel of rural Australia and old fashioned vibe. The flyer should highlight our services and our "free quote" policy. Attached is my business logo.

Industry/Entity Type

Small Business

Font styles to use
Serif
Decorative

Colors
f37122
fcca95
ec1f27
abd036
9bcb3c

Requirements
Must have
• A list of our services and all my contact information as well as our offer for free quotes. Present this flyer and customer receives first hour of gardening free
Nice to have
• I would like the overall feel of the design to be old fashioned. Think old painted advertisments for wickam soap and brennicks biscuits, or an old dorvan pick-up truck with the dog in the back, want to highlight our quality but also give my customers a feel for our brand as a whole

```html
<!DOCTYPE html>
<html lang="en">
<head>
<meta charset="utf-8">
<title>Tallowbend Garden Care – Flyer</title>
<link href="https://fonts.googleapis.com/css2?family=Josefin+Sans:wght@300;400;600&family=Oswald:wght@500;700&family=Kaushan+Script&display=swap" rel="stylesheet">
<style>
  :root {
    --backdrop: #e8e2d8;
    --paper-light: #f0d49a;
    --paper-mid: #e2b66c;
    --paper-edge: #c98c3e;
    --maroon: #7a1418;
    --deep-red: #8b1a1e;
    --ink: #3b2416;
    --frame-dark: #2a2218;
    --wood-light: #b49e86;
    --wood-dark: #6e5b49;
    --cream: #fbf3e2;
    --photo-light: #d8d2c6;
    --photo-dark: #6d675e;
    --rose-pink: #d98aa8;
    --rose-leaf: #7d9a55;
    --social-blue: #3b5a96;
  }
  * { box-sizing: border-box; margin: 0; padding: 0; }
  html, body { width: 1200px; height: 500px; overflow: hidden; background: var(--backdrop); }
  .canvas { position: relative; width: 1200px; height: 500px; font-family: "Josefin Sans", sans-serif; color: var(--maroon); }

  .flyer {
    position: absolute; top: 30px; height: 436px;
    background: radial-gradient(ellipse at 50% 45%, var(--paper-light) 0%, var(--paper-mid) 65%, var(--paper-edge) 100%);
    box-shadow: 0 2px 6px rgba(0,0,0,.25);
  }
  .flyer--front { left: 22px; width: 562px; }
  .flyer--back { left: 613px; width: 558px; }

  .border-frame { position: absolute; inset: 0; pointer-events: none; }

  .brand-block {
    position: absolute; background: var(--paper-light);
    border: 7px solid var(--frame-dark);
    display: flex; flex-direction: column; align-items: center; justify-content: center; text-align: center;
    font-family: "Josefin Sans", sans-serif; font-weight: 600; color: var(--maroon); line-height: 1.15;
  }
  .flyer--front .brand-block { left: 193px; top: 18px; width: 175px; height: 137px; font-size: 23px; }
  .flyer--back .brand-block { left: 174px; top: 20px; width: 213px; height: 165px; font-size: 29px; }

  .tagline-box {
    position: absolute; left: 50px; top: 117px; width: 135px; height: 110px;
    background: var(--deep-red); color: var(--cream);
    font-size: 13px; letter-spacing: .5px; line-height: 1.55; text-align: center;
    display: flex; align-items: center; justify-content: center; text-transform: uppercase;
  }

  .truck-photo {
    position: absolute; left: 23px; top: 235px; width: 247px; height: 180px;
    background: radial-gradient(ellipse at 45% 45%, var(--photo-light) 0%, #a9a398 60%, var(--photo-dark) 100%);
    -webkit-mask-image: radial-gradient(ellipse at 50% 50%, #000 65%, transparent 100%);
            mask-image: radial-gradient(ellipse at 50% 50%, #000 65%, transparent 100%);
  }

  .abn { position: absolute; left: 378px; top: 66px; font-size: 12.5px; color: var(--maroon); }
  .follow { position: absolute; left: 398px; top: 90px; font-size: 12.5px; letter-spacing: 1px; color: var(--ink); }
  .social-link {
    position: absolute; left: 392px; top: 116px; width: 100px;
    display: flex; align-items: center; justify-content: center; gap: 5px;
    font-size: 12.5px; color: var(--maroon);
  }
  .social-link__square { width: 12px; height: 12px; background: var(--social-blue); flex: none; }

  .services { position: absolute; left: 318px; top: 163px; list-style: none; font-size: 15px; line-height: 21.5px; color: var(--maroon); }
  .services li { display: flex; align-items: center; gap: 5px; }
  .services svg { width: 16px; height: 10px; flex: none; }

  .contact-board {
    position: absolute; left: 318px; top: 255px; width: 181px; height: 165px;
    background: linear-gradient(180deg, var(--wood-light) 0%, #8f7a66 45%, var(--wood-dark) 100%);
    text-align: center; color: #fff; padding-top: 9px;
  }
  .contact-board__call { font-family: "Kaushan Script", cursive; font-size: 17px; line-height: 23px; text-shadow: 1px 1px 2px rgba(0,0,0,.5); }
  .contact-board__name { font-family: "Oswald", sans-serif; font-weight: 500; font-size: 13px; margin-top: 2px; }
  .contact-board__phone { font-family: "Oswald", sans-serif; font-weight: 500; font-size: 18px; margin-top: 9px; display: flex; justify-content: center; align-items: center; gap: 5px; }
  .contact-board__phone svg { width: 15px; height: 15px; }

  .location { position: absolute; left: 408px; top: 108px; font-size: 13.5px; line-height: 19px; color: var(--maroon); }
  .location svg { width: 9px; height: 12px; vertical-align: -1px; margin-right: 2px; }

  .pitch {
    position: absolute; left: 20px; top: 213px; width: 518px; text-align: center;
    font-size: 15.5px; font-weight: 300; line-height: 18px; color: var(--ink); letter-spacing: .2px;
  }

  .roses {
    position: absolute; left: 147px; top: 278px; width: 258px; height: 122px;
    background: radial-gradient(ellipse at 50% 50%, var(--rose-pink) 0%, #c992a6 35%, var(--rose-leaf) 65%, transparent 80%);
  }

  .back-phone {
    position: absolute; left: 0; right: 0; top: 386px; text-align: center;
    font-family: "Oswald", sans-serif; font-weight: 700; font-size: 29px; line-height: 36px; color: var(--maroon);
    display: flex; justify-content: center; align-items: center; gap: 6px;
  }
  .back-phone svg { width: 24px; height: 24px; }
</style>
</head>
<body>
<div class="canvas">

  <section class="flyer flyer--front">
    <svg class="border-frame" viewBox="0 0 562 436" aria-hidden="true">
      <rect x="8" y="8" width="546" height="420" fill="none" stroke="#fbf3e2" stroke-width="1" stroke-dasharray="3 3"/>
      <rect x="18" y="18" width="526" height="400" fill="none" stroke="var(--frame-dark)" stroke-width="1.5"/>
    </svg>

    <div class="brand-block">Tallowbend<br>Garden Care</div>

    <div class="tagline-box">Quality<br>gardening<br>by<br>skilled<br>professionals</div>

    <div class="truck-photo" role="img" aria-label="Sepia photo of an old dorvan pick-up truck with a dog in the back"></div>

    <p class="abn">ABN:31 507 294 618</p>
    <p class="follow">Follow Us On</p>
    <p class="social-link"><span class="social-link__square"></span>Tallowbend</p>

    <ul class="services">
      <li><svg viewBox="0 0 16 10"><path d="M1 5h11M8 1l5 4-5 4" fill="none" stroke="currentColor" stroke-width="1.6"/></svg>Garden Maintenance</li>
      <li><svg viewBox="0 0 16 10"><path d="M1 5h11M8 1l5 4-5 4" fill="none" stroke="currentColor" stroke-width="1.6"/></svg>Horticulture</li>
      <li><svg viewBox="0 0 16 10"><path d="M1 5h11M8 1l5 4-5 4" fill="none" stroke="currentColor" stroke-width="1.6"/></svg>Landscaping</li>
      <li><svg viewBox="0 0 16 10"><path d="M1 5h11M8 1l5 4-5 4" fill="none" stroke="currentColor" stroke-width="1.6"/></svg>Design</li>
    </ul>

    <div class="contact-board">
      <p class="contact-board__call">Contact Us<br>For A Free Quote<br>Today</p>
      <p class="contact-board__name">Maren Holloway</p>
      <p class="contact-board__phone">
        <svg viewBox="0 0 24 24"><circle cx="12" cy="12" r="10" fill="none" stroke="#fff" stroke-width="2"/><path d="M9 7c-1 1-1 3 1 6s4 4 5 4l1.5-1.5-2-2-1 .5c-1-.5-2-2-2.5-3l.5-1-2-2z" fill="#fff"/></svg>
        0491555207
      </p>
    </div>
  </section>

  <section class="flyer flyer--back">
    <svg class="border-frame" viewBox="0 0 558 436" aria-hidden="true">
      <rect x="13" y="13" width="532" height="410" fill="none" stroke="var(--deep-red)" stroke-width="2" stroke-dasharray="5 4"/>
      <line x1="13" y1="315" x2="545" y2="315" stroke="#fbf3e2" stroke-width="1" stroke-dasharray="5 4"/>
    </svg>

    <div class="brand-block">Tallowbend<br>Garden Care</div>

    <p class="location">
      <svg viewBox="0 0 10 13"><path d="M5 0a4.5 4.5 0 0 0-4.5 4.5C.5 8 5 13 5 13s4.5-5 4.5-8.5A4.5 4.5 0 0 0 5 0zm0 6.3a1.8 1.8 0 1 1 0-3.6 1.8 1.8 0 0 1 0 3.6z" fill="currentColor"/></svg>Wattlebrook St<br>Canberra, ACT
    </p>

    <p class="pitch">Tallowbend will help you in your yard, from a little TLC<br>all the way to design and construction of a completely<br>new outdoor space, call for a free quote!</p>

    <div class="roses" role="img" aria-label="Painted pink roses with leaves draped over a small grey banner"></div>

    <p class="back-phone">
      <svg viewBox="0 0 24 24"><circle cx="12" cy="12" r="10" fill="none" stroke="currentColor" stroke-width="2"/><path d="M9 7c-1 1-1 3 1 6s4 4 5 4l1.5-1.5-2-2-1 .5c-1-.5-2-2-2.5-3l.5-1-2-2z" fill="currentColor"/></svg>
      0491555207
    </p>
  </section>

</div>
</body>
</html>
```